Corvane spray foam and Environmental

I have business cards but need new ones. The ones I have are very bland. Here is. Y company website http://www.corvanesprayfoam.ca

Also I can send you copies of the current cards
I would also need my current logo on the new design as well.. Also spray foam and Environmental

Industry/Entity Type

Business

Logo Text

Corvane.

```html
<!DOCTYPE html>
<html lang="en">
<head>
<meta charset="utf-8">
<title>Corvane Spray Foam Ltd. — Business Cards</title>
<link rel="stylesheet" href="https://fonts.googleapis.com/css2?family=Work+Sans:wght@400;500;700&family=Tinos&display=swap">
<style>
  :root {
    --backdrop: #262628;
    --card: #1c1c1e;
    --purple: #7e3fa6;
    --silver: #d6d6d8;
    --text-light: #d4d4d6;
    --text-muted: #9a9a9e;
    --tagline: #8e8e92;
  }
  * { margin: 0; padding: 0; box-sizing: border-box; }
  html, body { width: 1200px; height: 738px; overflow: hidden; }
  body {
    background: var(--backdrop);
    font-family: "Work Sans", sans-serif;
    position: relative;
  }
  .card {
    position: absolute;
    width: 540px;
    height: 308px;
    background: var(--card);
    border-radius: 4px;
    overflow: hidden;
    box-shadow: 0 10px 30px rgba(0,0,0,.45);
  }
  .card--back { left: 40px; top: 215px; }
  .card--front { left: 620px; top: 215px; }

  .brand { position: absolute; }
  .brand__row { display: flex; align-items: center; gap: 10px; }
  .brand__mark {
    width: 34px; height: 34px;
    background: var(--silver);
    border-radius: 4px;
  }
  .brand__name {
    font-family: "Work Sans", sans-serif;
    font-weight: 700;
    color: var(--purple);
    font-size: 26px;
    letter-spacing: 1px;
    line-height: 1;
  }
  .brand__tagline {
    font-family: "Tinos", serif;
    color: var(--tagline);
    font-size: 21px;
    margin-top: 6px;
    white-space: nowrap;
  }
  .card--back .brand { left: 150px; top: 100px; }
  .card--back .website {
    position: absolute;
    left: 0; right: 0; top: 236px;
    text-align: center;
    color: var(--text-light);
    font-size: 13px;
    letter-spacing: 1px;
  }

  .card--front .brand { left: 40px; top: 118px; }
  .card--front .brand__name { font-size: 22px; }
  .card--front .brand__mark { width: 30px; height: 30px; }
  .card--front .brand__tagline { font-size: 18px; }

  .divider {
    position: absolute;
    left: 318px; top: 60px;
    width: 2px; height: 140px;
    background: var(--purple);
  }
  .contact { position: absolute; left: 340px; top: 52px; }
  .contact__name {
    color: var(--purple);
    font-weight: 500;
    font-size: 18px;
    letter-spacing: 1.5px;
  }
  .contact__role {
    color: var(--text-light);
    font-size: 12px;
    font-weight: 500;
    margin-top: 4px;
  }
  .contact__address {
    color: var(--text-muted);
    font-size: 11px;
    line-height: 1.35;
    margin-top: 14px;
  }
  .contact__list { list-style: none; margin-top: 10px; }
  .contact__item {
    display: flex; align-items: center; gap: 8px;
    color: var(--text-light);
    font-size: 12px;
    line-height: 1.45;
  }
  .contact__icon { width: 9px; height: 9px; flex: none; }
  .bands { position: absolute; left: 0; bottom: 0; }
</style>
</head>
<body>

<section class="card card--back" aria-label="Card back">
  <div class="brand">
    <div class="brand__row">
      <span class="brand__mark"></span>
      <span class="brand__name">CORVANE</span>
    </div>
    <div class="brand__tagline">Residential &amp; Commercial</div>
  </div>
  <p class="website">www.corvanesprayfoam.ca</p>
</section>

<section class="card card--front" aria-label="Card front">
  <div class="brand">
    <div class="brand__row">
      <span class="brand__mark"></span>
      <span class="brand__name">CORVANE</span>
    </div>
    <div class="brand__tagline">Residential &amp; Commercial</div>
  </div>

  <span class="divider"></span>

  <div class="contact">
    <h1 class="contact__name">DARREN HOLT</h1>
    <p class="contact__role">Founder</p>
    <p class="contact__address">4820 Alder Road Surrey,<br>British Columbia v3r 2k9, CA</p>
    <ul class="contact__list">
      <li class="contact__item">
        <svg class="contact__icon" viewBox="0 0 10 10"><path d="M2 1 L4 1 L4.5 3 L3.5 4 Q4.5 6 6 6.5 L7 5.5 L9 6 L9 8 Q5 9 2 5.5 Q1 3.5 2 1Z" fill="var(--purple)"/></svg>
        (604) 555-0182
      </li>
      <li class="contact__item">
        <svg class="contact__icon" viewBox="0 0 10 10"><rect x="1" y="2" width="8" height="6" fill="none" stroke="var(--purple)" stroke-width="1.2"/><path d="M1 2 L5 5.5 L9 2" fill="none" stroke="var(--purple)" stroke-width="1.2"/></svg>
        corvanefoam@mail.com
      </li>
      <li class="contact__item">
        <svg class="contact__icon" viewBox="0 0 10 10"><circle cx="5" cy="5" r="4" fill="var(--purple)"/></svg>
        www.corvanesprayfoam.ca
      </li>
    </ul>
  </div>

  <svg class="bands" width="540" height="80" viewBox="0 0 540 80" aria-hidden="true">
    <polygon points="0,56 370,56 358,72 0,72" fill="var(--silver)"/>
    <polygon points="395,46 540,18 540,52 372,52" fill="var(--purple)"/>
  </svg>
</section>

</body>
</html>
```